Creating the Look and Feel of an Elite Boutique Consulting Practice: Vane Advisory

Complete a professional website on Weebly. As part of the site, we are open to a new logo -- we have just launched. We put up a starter website that shows you the content and theme we are going for. But clearly we aren't professional web designers and we need your help. Check out our start at vaneadvisory.com

Target Market(s)

Fortune 500 Clients

Industry/Entity Type

Management Consulting

Logo Text

VANE Advisory

Number of Pages Required

4 page

Requirements
Must have
• I've already set us up on Weebly. I'd like to give the selected designer the log-in credentials and have the designer create it on Weebly, so we can maintain it through that service.

```html
<!DOCTYPE html>
<html lang="en">
<head>
<meta charset="utf-8">
<title>Vane Advisory</title>
<link rel="stylesheet" href="https://fonts.googleapis.com/css2?family=Questrial&display=swap">
<style>
  :root {
    --frame: #650000;
    --maroon: #6e0a0a;
    --brand: #9c1a1a;
    --rule: #a31616;
    --pink: #ee6f7c;
    --ink: #5a0000;
    --white: #ffffff;
    --footer: #3e0000;
  }
  * { margin: 0; padding: 0; box-sizing: border-box; }
  html, body { width: 986px; height: 1200px; overflow: hidden; }
  body {
    background: var(--frame);
    font-family: "Questrial", "Century Gothic", sans-serif;
    color: var(--ink);
  }
  .page {
    position: absolute; left: 38px; top: 0; width: 912px; height: 1200px;
    background: var(--white);
  }
  .site-header { position: relative; height: 113px; }
  .main-nav a {
    position: absolute; top: 70px;
    color: var(--ink); text-decoration: none; font-size: 17px; letter-spacing: -0.2px;
  }
  .nav-rule { position: absolute; top: 100px; height: 2px; background: var(--rule); }
  .brand {
    position: absolute; left: 365px; top: 60px; width: 182px;
    display: flex; align-items: center; justify-content: center; gap: 6px;
    color: var(--brand); font-size: 19px; font-weight: 400; letter-spacing: 0.3px; white-space: nowrap;
  }
  .brand-mark { width: 12px; height: 12px; background: var(--brand); }
  .headline-band {
    height: 101px;
    background: linear-gradient(#560000, #862420);
    border-top: 1px solid #3a0000;
    display: flex; align-items: center; justify-content: center; text-align: center;
  }
  .headline-band h1 {
    color: var(--white); font-weight: 400; font-size: 32px; line-height: 39px;
    text-shadow: 0 2px 4px rgba(0,0,0,.55);
  }
  .hero {
    height: 608px;
    background: radial-gradient(ellipse at 55% 45%, #f7f6f8 0%, #e6e3e7 60%, #d7d3d8 100%);
  }
  .intro {
    position: relative; height: 335px;
    border-top: 2px solid var(--maroon);
    font-size: 12.6px; line-height: 15.8px;
  }
  .intro h2 { color: var(--pink); font-weight: 400; font-size: 16px; line-height: 19.5px; }
  .intro-col { position: absolute; top: 28px; }
  .col-people { left: 19px; width: 422px; }
  .col-help { left: 468px; width: 425px; }
  .trait { margin-top: 14px; }
  .col-people h2 { margin-bottom: 26px; }
  .trait h3 { font-size: 12.6px; font-weight: 700; }
  .trait p, .closing { font-style: italic; }
  .intro a { color: var(--ink); }
  .col-help h2 { margin-bottom: 7px; }
  .col-help li { list-style: none; margin-bottom: 15.5px; }
  .closing { position: absolute; left: 468px; top: 299px; }
  .site-footer {
    position: absolute; left: 0; top: 1157px; width: 912px; height: 43px;
    background: var(--footer);
    display: flex; align-items: center; padding-left: 20px;
    font-size: 13.5px;
  }
  .site-footer a, .site-footer span { color: var(--pink); text-decoration: none; }
  .site-footer a { padding: 0 23px; border-right: 1px solid #6b1010; line-height: 20px; }
  .site-footer a:first-child { padding-left: 0; }
  .site-footer a:last-of-type { border-right: none; }
  .site-footer span { margin-left: 8px; }
</style>
</head>
<body>
<div class="page">
  <header class="site-header">
    <nav class="main-nav">
      <a href="#" style="left:102px">ABOUT VANE</a>
      <a href="#" style="left:226px">APPROACH</a>
      <a href="#" style="left:598px">OUR TEAM</a>
      <a href="#" style="left:709px">CONTACT US</a>
    </nav>
    <div class="nav-rule" style="left:77px;width:289px"></div>
    <div class="nav-rule" style="left:547px;width:289px"></div>
    <div class="brand"><span class="brand-mark"></span>VANE ADVISORY</div>
  </header>

  <section class="headline-band">
    <h1>Do you need to<br>transform your organization?</h1>
  </section>

  <div class="hero" role="img" aria-label="Colourful 3D letter blocks spelling clinical leadership, audit, management and quality improvement, with the words purpose-led organizational transformation"></div>

  <section class="intro">
    <div class="intro-col col-people">
      <h2>The people of VANE ADVISORY are:</h2>
      <div class="trait">
        <h3>Experienced.</h3>
        <p>Over the past three decades, we have deep experience driving organizational transformation in more than 33 countries, for some of the world’s largest, most transformative companies in your industry.</p>
      </div>
      <div class="trait" style="margin-top:24px">
        <h3>Curious.</h3>
        <p>Each of the dozens of transformations we’ve enabled are unique. Our most relevant experience is our ability to listen and learn where you want to go, and to partner with you to create an original set of tools and experiences to help your people get there. If you’re curious, <a href="#">learn more about our team.</a></p>
      </div>
      <div class="trait" style="margin-top:24px">
        <h3>Ready to Hear Your Story.</h3>
        <p>Of course the best way to get to know more about us is to <a href="#">contact us</a>, talk to us and see what you think.</p>
      </div>
    </div>
    <div class="intro-col col-help">
      <h2>We help your organization achieve a successful, resilient transformation by:</h2>
      <ul>
        <li>Partnering with you to clarify and communicate your transformational purpose.</li>
        <li>Assessing the current state of your organization.</li>
        <li>Building innovative engagements to help people master the skillets and mindsets needed for your current and future context.</li>
        <li>Embedding routines and practices to ensure the transformation is structurally resilient.</li>
      </ul>
    </div>
    <p class="closing">So, why not <a href="#">read more</a> about our approach?</p>
  </section>

  <footer class="site-footer">
    <a href="#">ABOUT VANE</a>
    <a href="#">APPROACH</a>
    <a href="#">OUR TEAM</a>
    <a href="#">CONTACT US</a>
    <span>© Vane Advisory, All rights reserved.</span>
  </footer>
</div>
</body>
</html>
```